New letter head for Air Conditioning business

We need a new professional letter head design to suit our new re-branded air conditioning business. Our new logo is attached

```html
<!DOCTYPE html>
<html lang="en">
<head>
<meta charset="utf-8">
<title>Nordvale Letterhead</title>
<link href="https://fonts.googleapis.com/css2?family=Lato:wght@300;400;700&family=Pinyon+Script&display=swap" rel="stylesheet">
<style>
  :root {
    --backdrop: #e4e4e4;
    --paper: #f2f2f2;
    --ink: #3a3a3a;
    --ink-strong: #111111;
    --brand-green: #5cb47c;
    --brand-red: #e2635a;
    --brand-dark: #333333;
  }
  * { margin: 0; padding: 0; box-sizing: border-box; }
  html, body {
    width: 1200px; height: 1200px; overflow: hidden;
    background: var(--backdrop);
    font-family: "Lato", sans-serif;
  }
  .letterhead {
    position: absolute; left: 197px; top: 30px;
    width: 806px; height: 1140px;
    background: var(--paper);
    box-shadow: 0 6px 24px rgba(0,0,0,0.12);
  }
  .brand {
    position: absolute; top: 62px; left: 0; width: 100%;
    display: flex; justify-content: center; align-items: center; gap: 14px;
  }
  .brand-dot { width: 46px; height: 46px; border-radius: 50%; background: var(--brand-green); }
  .brand-text { display: flex; flex-direction: column; }
  .brand-name {
    font-size: 34px; font-weight: 700; letter-spacing: 3px; line-height: 1;
    color: var(--brand-dark); text-transform: uppercase;
  }
  .brand-tagline {
    margin-top: 6px; font-size: 7px; font-weight: 700; letter-spacing: 1.6px;
    color: var(--brand-green); text-transform: uppercase;
  }
  .letter {
    position: absolute; left: 86px; width: 634px;
    font-size: 12.6px; font-weight: 300; color: var(--ink); line-height: 19px;
  }
  .date { top: 270px; }
  .recipient { top: 308px; }
  .recipient strong { font-weight: 700; color: var(--ink-strong); }
  .salutation { top: 403px; }
  .body-text { top: 440px; }
  .body-text p { text-align: justify; margin-bottom: 19px; }
  .closing { top: 858px; }
  .signature {
    position: absolute; left: 92px; top: 876px;
    font-family: "Pinyon Script", cursive; font-size: 27px; color: var(--ink-strong);
  }
  .footer {
    position: absolute; left: 0; top: 1068px; width: 100%;
    text-align: center; font-size: 13px; color: var(--brand-dark); line-height: 18px;
  }
  .contacts { display: flex; justify-content: center; align-items: center; gap: 8px; }
  .contact { display: inline-flex; align-items: center; gap: 5px; }
  .contact svg { width: 10px; height: 10px; }
  .colour-bar {
    position: absolute; left: 0; bottom: 0; width: 100%; height: 15px; display: flex;
  }
  .colour-bar span { flex: 1; }
  .bar-green { background: var(--brand-green); }
  .bar-red { background: var(--brand-red); }
  .bar-dark { background: var(--brand-dark); }
</style>
</head>
<body>
<main class="letterhead">
  <header class="brand">
    <div class="brand-dot"></div>
    <div class="brand-text">
      <span class="brand-name">Nordvale</span>
      <span class="brand-tagline">Air Conditioning &amp; Refrigeration</span>
    </div>
  </header>

  <div class="letter date">01 January 2050</div>
  <div class="letter recipient">
    <strong>Company (Pvt) Ltd.</strong><br>
    PO Box 3355 Mainville St<br>
    Sample City Country 3355
  </div>
  <div class="letter salutation">Dear Daniel Marsh,</div>

  <section class="letter body-text">
    <p>Lorem ipsum dolor sit amet, consectetuer adipiscing elit, sed diam nonummy nibh euismod tincidunt ut laoreet dolore magna aliquam erat volutpat. Ut wisi enim ad minim veniam, quis nostrud exerci tation ullamcorper suscipit lobortis nisl ut aliquip ex ea commodo consequat. Duis dolore te feugait nulla facilisi. Nam liber tempor cum soluta nobis eleifend option congue nihil imperdiet doming id quod mazim placerat facer possim assum. Lorem ipsum dolor sit amet, consectetuer adipiscing elit, sed diam nonummy nibh euismod tincidunt ut laoreet dolore magna aliquam erat volutpat. Ut wisi enim ad minim veniam, quis nostrud exerci tation ullamcorper suscipit lobortis nisl ut aliquip ex ea commodo consequat.</p>
    <p>Consectetuer adipiscing elit, sed diam nonummy nibh euismod tincidunt ut laoreet dolore magna aliquam erat volutpat. Ut wisi enim ad minim veniam, quis nostrud exerci tation ullamcorper suscipit lobortis nisl ut aliquip ex ea commodo consequat. Consectetuer adipiscing elit, sed diam nonummy nibh euismod tincidunt ut laoreet dolore magna aliquam erat volutpat. Ut wisi enim ad minim veniam, quis nostrud exerci tation ullamcorper suscipit lobortis nisl ut aliquip ex ea commodo consequat.</p>
    <p>Consectetuer adipiscing elit, sed diam nonummy nibh euismod tincidunt ut laoreet dolore magna aliquam erat volutpat. Ut wisi enim ad minim veniam, quis nostrud exerci tation ullamcorper suscipit lobortis nisl ut aliquip ex ea commodo consequat. Consectetuer adipiscing elit, sed diam nonummy nibh euismod tincidunt ut laoreet dolore magna aliquam erat volutpat. Ut wisi enim ad minim veniam, quis nostrud exerci tation ullamcorper suscipit lobortis nisl ut aliquip ex ea commodo consequat.</p>
  </section>

  <div class="letter closing">Sincerely Yours</div>
  <div class="signature">Thomas Reid Calloway</div>

  <footer class="footer">
    <div class="address">Unit 14, Level 2, Harrow Lane, NSW, Australia 2000</div>
    <div class="contacts">
      <span class="contact">
        <svg viewBox="0 0 10 10"><path d="M2 1 L4 1 L4.6 3 L3.5 3.8 Q4.5 5.8 6.2 6.5 L7 5.4 L9 6 L9 8 Q8.5 9 7.5 9 Q1 8 1 2.5 Q1 1.5 2 1 Z" fill="var(--brand-green)"/></svg>
        (+61) 200 555 014
      </span>
      <span class="contact">
        <svg viewBox="0 0 10 10"><rect x="0.5" y="2" width="9" height="6" fill="var(--brand-green)"/><path d="M0.5 2 L5 5.5 L9.5 2" fill="none" stroke="var(--paper)" stroke-width="0.9"/></svg>
        info@nordvaleair.com
      </span>
      <span class="contact">
        <svg viewBox="0 0 10 10"><circle cx="5" cy="5" r="4.2" fill="none" stroke="var(--brand-green)" stroke-width="1"/><ellipse cx="5" cy="5" rx="1.8" ry="4.2" fill="none" stroke="var(--brand-green)" stroke-width="0.8"/><line x1="0.8" y1="5" x2="9.2" y2="5" stroke="var(--brand-green)" stroke-width="0.8"/></svg>
        www.nordvaleair.com
      </span>
    </div>
  </footer>

  <div class="colour-bar">
    <span class="bar-green"></span>
    <span class="bar-red"></span>
    <span class="bar-dark"></span>
  </div>
</main>
</body>
</html>
```